Daniel Fordyce Psychotherapy Business Card Design Project

I need a welcoming business card for a Somatic Psychotherapy private practice based in Melbourne, Australia. I help individual clients to work through issues in their life that are inhibiting achieving their full potential. I would like a san serif font and the oculars are:
blue: R:37 G:61 B:95 C:93 M:77 Y:38 K:28
orange: R:241 G:103 B:43 C:0 M:74 Y:93 K:0
The final design should communicate warm, welcoming and safe environment in which clients are supported to grow. It should also convey a collaborative approach to achieve success between me (the therapist) and the client. The uploaded file is my new logo. Also an organic look and feel while maintaining professionalism and a clean, simple look is sought after.
In addition to the logo my details are:
Daniel Fordyce
Psychotherapist
B.Arts., Grad Dip. T&D., Dip.Som.Psych, MRTOB, MFLENG
0417 552 908
dfordyce@danielfordyce.com.au
www.danielfordyce.com.au
Psychotherapy Clients
Environment

```html
<!DOCTYPE html>
<html lang="en">
<head>
<meta charset="utf-8">
<title>Daniel Fordyce Psychotherapy – Business Card</title>
<link rel="stylesheet" href="https://fonts.googleapis.com/css2?family=Source+Sans+3:ital,wght@0,400;0,500;0,600;1,700&display=swap">
<style>
  :root {
    --blue: #253d5f;
    --orange: #f1672b;
    --white: #ffffff;
    --ink: #2a3347;
    --backdrop: #000000;
  }
  * { margin: 0; padding: 0; box-sizing: border-box; }
  html, body { width: 1200px; height: 686px; overflow: hidden; background: var(--backdrop); }
  body { font-family: "Source Sans 3", sans-serif; position: relative; }

  .card {
    position: absolute;
    width: 507px;
    height: 289px;
    background: var(--white);
    overflow: hidden;
  }
  .card--front { left: 52px; top: 147px; }
  .card--back  { left: 617px; top: 347px; }

  .brand {
    position: absolute;
    left: 0;
    right: 0;
    text-align: center;
  }
  .card--front .brand { top: 52px; }
  .card--back  .brand { top: 100px; }
  .brand__name {
    color: var(--blue);
    font-weight: 600;
    font-size: 36px;
    line-height: 1.05;
    letter-spacing: 0.3px;
  }

  .band-marker {
    position: absolute;
    left: 0;
    width: 30px;
    background: var(--blue);
  }
  .band {
    position: absolute;
    left: 37px;
    right: 0;
    background: var(--orange);
    text-align: center;
  }
  .card--front .band-marker,
  .card--front .band { top: 180px; height: 44px; }
  .card--back .band-marker,
  .card--back .band { top: 247px; height: 29px; }

  .band__title {
    color: var(--white);
    font-weight: 700;
    font-style: italic;
    font-size: 16px;
    line-height: 1;
    padding-top: 6px;
  }
  .band__credentials {
    color: var(--ink);
    font-size: 12px;
    line-height: 1;
    margin-top: 5px;
  }
  .band__web {
    color: var(--white);
    font-size: 13px;
    line-height: 29px;
  }

  .contact {
    position: absolute;
    left: 0; right: 0;
    display: flex;
    justify-content: center;
    gap: 12px;
    color: var(--ink);
    font-size: 13px;
    line-height: 1;
  }
  .contact--phone { top: 236px; }
  .contact--online { top: 257px; }
  .contact__item { display: inline-flex; align-items: center; gap: 6px; }
  .contact__icon { width: 11px; height: 11px; fill: var(--blue); }
</style>
</head>
<body>

<section class="card card--front" aria-label="Card front">
  <div class="brand">
    <p class="brand__name">Daniel Fordyce<br>Psychotherapy</p>
  </div>

  <span class="band-marker"></span>
  <div class="band">
    <p class="band__title">Daniel Fordyce Psychotherapist</p>
    <p class="band__credentials">B.Arts. Grad Dip. T&amp;D., Dip.Som.Psych, MRTOB, MFLENG</p>
  </div>

  <div class="contact contact--phone">
    <span class="contact__item">
      <svg class="contact__icon" viewBox="0 0 24 24" aria-hidden="true"><path d="M6.6 10.8a15 15 0 0 0 6.6 6.6l2.2-2.2c.3-.3.7-.4 1-.2 1.1.4 2.3.6 3.6.6.6 0 1 .4 1 1V20c0 .6-.4 1-1 1A17 17 0 0 1 3 4c0-.6.4-1 1-1h3.5c.6 0 1 .4 1 1 0 1.3.2 2.5.6 3.6.1.3 0 .7-.2 1z"/></svg>
      0417 552 908
    </span>
  </div>
  <div class="contact contact--online">
    <span class="contact__item">
      <svg class="contact__icon" viewBox="0 0 24 24" aria-hidden="true"><path d="M2 9l10-6 10 6v11a1 1 0 0 1-1 1H3a1 1 0 0 1-1-1zm2 1.2V19h16v-8.8l-8 5z"/></svg>
      dfordyce@danielfordyce.com.au
    </span>
    <span class="contact__item">
      <svg class="contact__icon" viewBox="0 0 24 24" aria-hidden="true"><path d="M12 2a10 10 0 1 0 0 20 10 10 0 0 0 0-20zM3.5 9h17v2h-17zm0 4h17v2h-17z"/></svg>
      www.danielfordyce.com.au
    </span>
  </div>
</section>

<section class="card card--back" aria-label="Card back">
  <div class="brand">
    <p class="brand__name">Daniel Fordyce<br>Psychotherapy</p>
  </div>

  <span class="band-marker"></span>
  <div class="band">
    <p class="band__web">www.danielfordyce.com.au</p>
  </div>
</section>

</body>
</html>
```